The Lantern Over The Hills

This is a book about the growth of a father and how that can help us relate to our Heavenly Father. It's a Christian growth and/or self-help book, talking about experiences any father might go through, the ups and downs, the triumphs and struggles of life. Something we can all relate to.

I would prefer some artwork like the attached - showing a father with 2 or 3 kids, no faces. Something colorful and catchy.

The subhead would be:

When Little Ones Show Us How To Trust,
Rest & Walk Beside The Shepherd

By Doug Pettersen

```html
<!DOCTYPE html>
<html lang="en">
<head>
<meta charset="utf-8">
<title>The Lantern Over The Hills — Book Cover</title>
<link rel="stylesheet" href="https://fonts.googleapis.com/css2?family=Cinzel:wght@400;500&family=EB+Garamond:wght@400;500&display=swap">
<style>
  :root {
    --page-bg: #e4e4e6;
    --cover-bg: #f8f5ef;
    --gold: #c9a21a;
    --gold-deep: #7a5a08;
    --subtitle-red: #8e2c1c;
    --wash-pink: #d81c8c;
    --wash-orange: #f39a1e;
    --wash-yellow: #f7c73a;
    --wash-red: #e8432a;
  }
  * { box-sizing: border-box; margin: 0; padding: 0; }
  html, body {
    width: 1200px; height: 900px; overflow: hidden;
    background: var(--page-bg);
  }
  .cover {
    position: absolute;
    left: 320px; top: 30px;
    width: 560px; height: 840px;
    background: var(--cover-bg);
    text-align: center;
  }
  .title {
    position: absolute; left: 0; right: 0; top: 44px;
    font-family: "Cinzel", "Trajan Pro", serif;
    font-weight: 500;
    color: var(--gold);
    text-shadow: 1px 1px 0 var(--gold-deep);
    line-height: 1;
  }
  .title .small { display: block; font-size: 36px; letter-spacing: 3px; margin-bottom: 8px; }
  .title .large { display: block; font-size: 74px; letter-spacing: 3px; margin-bottom: 8px; }
  .title .mid { display: block; font-size: 30px; letter-spacing: 4px; margin-bottom: 8px; }
  .artwork {
    position: absolute; left: 100px; top: 290px;
    width: 420px; height: 400px;
    background:
      radial-gradient(ellipse 30% 34% at 30% 70%, var(--wash-pink) 0%, rgba(216,28,140,0.5) 55%, rgba(216,28,140,0) 100%),
      radial-gradient(ellipse 20% 26% at 78% 46%, var(--wash-red) 0%, rgba(232,67,42,0.4) 55%, rgba(232,67,42,0) 100%),
      radial-gradient(ellipse 36% 40% at 55% 64%, var(--wash-orange) 0%, rgba(243,154,30,0.55) 55%, rgba(243,154,30,0) 100%),
      radial-gradient(ellipse 30% 48% at 50% 36%, var(--wash-yellow) 0%, rgba(247,199,58,0.3) 60%, rgba(247,199,58,0) 100%);
  }
  .subtitle {
    position: absolute; left: 0; right: 0; top: 696px;
    font-family: "EB Garamond", Georgia, serif;
    font-size: 21px; line-height: 31px;
    color: var(--subtitle-red);
  }
  .author {
    position: absolute; left: 0; right: 0; top: 784px;
    font-family: "Cinzel", "Trajan Pro", serif;
    font-size: 28px; letter-spacing: 0.5px;
    color: var(--gold);
    text-shadow: 1px 1px 0 var(--gold-deep);
  }
</style>
</head>
<body>
  <main class="cover">
    <h1 class="title">
      <span class="small">The</span>
      <span class="large">Lantern</span>
      <span class="mid">Over The</span>
      <span class="large">Hills</span>
    </h1>
    <div class="artwork" role="img" aria-label="Watercolour silhouette of a father carrying a child on his shoulders beside a running daughter and a blossoming tree, in pink, orange and yellow washes"></div>
    <p class="subtitle">When Little Ones Show Us How To Trust,<br>Rest &amp; Walk Beside The Shepherd</p>
    <p class="author">BY DOUG PETTERSEN</p>
  </main>
</body>
</html>
```